UI/UX design for non-profit education/student success foundation website

Looking to work with a ui/ux designer that can provide an elegant, impactful and modern responsive design for a non-profit education/student success foundation website. The website will need to have a lot of visuals and elements with impactful statements. The responsive templates will later be parsed (this will be done by another developer) and converted to Concrete5 CMS templates. The organization likes bold colors with a modern sleek design. Typography is also key in titles and statements of interest. On-scroll visuals could be nice if it lends well to combining imagery and text. The site will need templates for a homepage, global sub-page, and contact page. Interchangeable block elements would be nice if we want to create other templates or change element positions.

Target Market(s)

Continued education and philanthropy individuals/organizations

Industry/Entity Type

Non-profit / college education

Coding

Coded - Design and coding required

Number of Pages Required

3 page

Font styles to use
Sans Serif
Script

Colors
0094D4
00A9DD
6FCCEA
C7EBF8
E9F6FB
59FF00
82FF00
B8FF75
E3FFCB
F4FFEA
FFC000
F8CF3A
FAE287
FDF2CF
FEFAEE
EE7325
F08F49
F5BC92
FAE3D3
FDF4ED
6B429C
8869AF
B7A5CE
E3DAEB
F3F0F8

Requirements
Must have
• Modern responsive design, impactful visual elements, available theme elements pre styled for things like forms, buttoms, tables...
Nice to have
• Onscroll vidual effects, heros with background video

```html
<!DOCTYPE html>
<html lang="en">
<head>
<meta charset="utf-8">
<title>The Halden Foundation</title>
<link href="https://fonts.googleapis.com/css2?family=Montserrat:ital,wght@0,300;0,400;0,500;0,600;0,700;1,400;1,600&family=Teko:wght@400;500&display=swap" rel="stylesheet">
<style>
:root{
  --navy:#0b4f74;
  --navy-deep:#073e5e;
  --ocean:#0a6a97;
  --cyan:#12c3ea;
  --sky:#00a9dd;
  --green:#7cc20f;
  --orange:#ee7325;
  --amber:#ffb300;
  --white:#ffffff;
  --ink:#1c3f58;
  --display:'Teko',sans-serif;
  --body:'Montserrat',sans-serif;
}
*{margin:0;padding:0;box-sizing:border-box}
html,body{width:1200px;height:5141px;overflow:hidden;background:#fff}
.page{position:relative;width:1200px;height:5141px;font-family:var(--body);color:var(--white);overflow:hidden}
.abs{position:absolute}
.photo{position:absolute}
.display{font-family:var(--display);font-weight:500;line-height:.95;letter-spacing:.5px}
.btn{position:absolute;display:flex;align-items:center;justify-content:center;border-radius:24px;font-size:13px;font-weight:700;letter-spacing:1px;color:#fff}
.btn-navy{background:var(--navy)}
.btn-green{background:var(--green)}
.btn-orange{background:var(--orange)}
.underline{position:absolute;height:3px;width:50px;background:var(--orange)}

/* header */
.brand{position:absolute;left:120px;top:14px;display:flex;align-items:center;gap:12px}
.brand-dot{width:40px;height:40px;border-radius:50%;background:var(--orange)}
.brand-name{font-family:var(--body);font-weight:700;font-size:21px;line-height:1.05;color:#fff;letter-spacing:.3px}
.nav a{position:absolute;top:32px;font-size:11.5px;font-weight:700;letter-spacing:.5px;color:#fff;text-decoration:none}
.nav a.active{border-bottom:2px solid var(--orange);padding-bottom:8px}

/* hero */
.hero{position:absolute;left:0;top:0;width:1200px;height:724px;background:linear-gradient(180deg,#3b3a3a 0%,#7a6556 45%,#4d4640 100%)}
.hero-shade{position:absolute;inset:0;background:radial-gradient(ellipse at 50% 45%,rgba(0,0,0,.05),rgba(0,0,0,.45))}
.play{position:absolute;left:579px;top:244px;width:56px;height:56px;border-radius:50%;background:var(--orange)}
.hero-title{position:absolute;left:0;width:1200px;top:318px;text-align:center;font-size:72px}
.hero-line1{position:absolute;left:0;width:1240px;top:386px;text-align:center;font-size:39px;font-weight:700}
.hero-line2{position:absolute;left:0;width:1240px;top:431px;text-align:center;font-size:39px;font-weight:300}

/* empower */
.empower{position:absolute;left:0;top:724px;width:1200px;height:530px;background:linear-gradient(90deg,#ffb300 0%,#f99a1c 45%,#ef7a22 100%)}
.empower-photo{position:absolute;right:0;top:0;width:560px;height:530px;background:linear-gradient(90deg,rgba(239,122,34,0) 0%,rgba(150,90,50,.35) 60%,rgba(110,70,50,.45) 100%)}
.empower-icon{position:absolute;left:574px;top:779px;width:24px;height:24px;border-radius:50%;border:4px solid #fff}
.empower-title{position:absolute;left:0;width:1190px;top:810px;text-align:center;font-size:54px}
.empower-sub{position:absolute;left:0;width:1190px;top:864px;text-align:center;font-size:33px;font-weight:300}
.empower-sub b{font-weight:700}
.empower-text{position:absolute;width:420px;font-size:14.5px;font-style:italic;line-height:1.75}

/* why */
.why{position:absolute;left:0;top:1250px;width:1200px;height:620px;background:var(--navy)}
.why-photo{position:absolute;left:420px;top:0;width:780px;height:620px;background:linear-gradient(90deg,rgba(11,79,116,1) 0%,rgba(40,90,110,.6) 30%,#5f7c88 55%,#b89a4c 80%,#6d7f86 100%)}
.why-title{position:absolute;left:152px;top:1368px;font-size:44px}
.why-sub1{position:absolute;left:152px;top:1422px;font-size:25px;font-weight:600}
.why-sub2{position:absolute;left:152px;top:1458px;font-size:25px;font-weight:400}
.why-text{position:absolute;left:152px;top:1512px;width:440px;font-size:14px;line-height:1.9}
.why-text b{font-weight:700}

/* services */
.section-title{position:absolute;color:var(--navy);text-align:center;font-size:52px}
.card{position:absolute;width:300px;height:240px;border-radius:44px 44px 44px 0;overflow:hidden}
.card-label{position:absolute;left:0;right:0;bottom:16px;text-align:center;font-weight:600;font-size:20px;color:#fff}
.c1{background:linear-gradient(160deg,#5c6a78,#1f2730)}
.c2{background:linear-gradient(160deg,#a8a39a,#4d4a44)}
.c3{background:linear-gradient(160deg,#7c7f83,#3a3634)}
.c4{background:linear-gradient(160deg,#7b5a43,#2f3b2e)}
.c5{background:linear-gradient(160deg,#c9ccd0,#7a2a2a 70%,#2a2a2a)}
.c6{background:linear-gradient(160deg,#f1f1ef,#d9c6a7 60%,#c58f3b)}
.card-fade{position:absolute;left:0;right:0;bottom:0;height:110px;background:linear-gradient(180deg,rgba(0,0,0,0),rgba(0,0,0,.65))}

/* testimonials */
.quote{position:absolute;width:442px;height:296px;border:5px solid #fff;border-radius:50px 50px 0 50px}
.avatar{position:absolute;left:38px;top:50px;width:66px;height:66px;border-radius:4px;background:linear-gradient(180deg,#d9cfc7,#8f7b6c)}
.quote-text{position:absolute;left:120px;top:46px;width:290px;font-size:13.5px;font-style:italic;font-weight:600;line-height:1.77}
.quote-by{position:absolute;left:120px;top:230px;font-size:14px;font-weight:700}

/* latest */
.news{position:absolute;width:306px;height:272px;border-radius:40px 40px 0 0;overflow:hidden}
.n1{background:linear-gradient(160deg,#8a8e92,#3b3f44)}
.n2{background:linear-gradient(160deg,#d2d0cc,#7a3a3a 70%,#3b3030)}
.n3{background:linear-gradient(160deg,#8e6b4f,#a03a2e 60%,#3e3a3a)}
.news-fade{position:absolute;left:0;right:0;bottom:0;height:150px;background:linear-gradient(180deg,rgba(0,0,0,0),rgba(0,0,0,.75))}
.news-date{position:absolute;left:24px;bottom:86px;background:var(--green);color:#fff;font-size:10px;font-weight:700;padding:3px 10px}
.news-text{position:absolute;left:26px;bottom:42px;width:250px;font-size:13px;font-weight:600;line-height:1.4;color:#fff}
.news-more{position:absolute;left:26px;bottom:18px;font-size:10px;font-weight:700;color:#fff}

/* feature */
.feature{position:absolute;left:0;top:3688px;width:1200px;height:560px;background:linear-gradient(90deg,#c9c3b9 0%,#9a8472 35%,#2c5d7b 55%,var(--navy) 75%)}
.feature-title{position:absolute;left:672px;top:3852px;font-size:46px}
.feature-text{position:absolute;left:672px;top:3978px;width:370px;font-size:13.5px;font-style:italic;line-height:1.8}
.feature-text b{font-weight:600}

/* support */
.support{position:absolute;left:0;top:4248px;width:1200px;height:560px;background:linear-gradient(90deg,#ffb300 0%,#f7911c 55%,#ef7a22 100%)}
.support-title{position:absolute;left:124px;top:4362px;font-size:46px}
.support-text{position:absolute;left:124px;top:4478px;width:400px;font-size:13.5px;line-height:1.8}
.support-text b{font-weight:700}
.support-photo{position:absolute;left:595px;top:4345px;width:485px;height:322px;border-radius:50px 50px 50px 0;background:linear-gradient(150deg,#c7c9c6 0%,#4a4040 40%,#a3252b 75%,#2b2020 100%)}

/* footer */
.footer{position:absolute;left:0;top:4822px;width:1200px;height:319px;background:var(--navy)}
.footer-brand{position:absolute;left:135px;top:4862px;display:flex;align-items:center;gap:12px}
.footer-about{position:absolute;left:138px;top:4975px;width:200px;font-size:11px;line-height:1.6}
.col-title{position:absolute;top:4852px;font-size:24px}
.col-links{position:absolute;top:4904px;font-size:12.5px;line-height:25px;list-style:none}
.rule{position:absolute;left:0;top:5092px;width:1200px;height:1px;background:rgba(255,255,255,.18)}
.copyright{position:absolute;left:0;width:1200px;top:5110px;text-align:center;font-size:10.5px;color:rgba(255,255,255,.75)}
</style>
</head>
<body>
<div class="page">

  <!-- hero -->
  <section class="hero">
    <div class="photo" style="inset:0;background:linear-gradient(120deg,#5a4a40,#a58a72 40%,#6c5a4c 70%,#3a3532)" role="img" aria-label="Students studying together around a table with books"></div>
    <div class="hero-shade"></div>
  </section>
  <div class="brand"><span class="brand-dot"></span><span class="brand-name">THE HALDEN<br>FOUNDATION</span></div>
  <nav class="nav">
    <a class="active" style="left:443px">SERVICES</a>
    <a style="left:579px">ABOUT US</a>
    <a style="left:716px">DONATE</a>
    <a style="left:843px">EDUCATION</a>
    <a style="left:993px">CONTACT</a>
  </nav>
  <div class="play"><svg width="56" height="56" viewBox="0 0 56 56"><path d="M24 19 L37 28 L24 37Z" fill="#fff"/></svg></div>
  <h1 class="hero-title display">Our Vision</h1>
  <p class="hero-line1">We are not giving up on educating</p>
  <p class="hero-line2">the world’s most childrens</p>

  <!-- empower -->
  <section class="empower">
    <div class="empower-photo" role="img" aria-label="Student smiling while studying at a desk"></div>
  </section>
  <div class="empower-icon"></div>
  <h2 class="empower-title display">We Empower</h2>
  <p class="empower-sub"><b>Education for</b> all childrens</p>
  <p class="empower-text" style="left:162px;top:948px">Lorem ipsum dolor sit amet, consectetur adipiscing elit, sed do eiusmod tempor incididunt ut labore et dolore magna aliqua. Ut enim ad minim veniam</p>
  <p class="empower-text" style="left:612px;top:944px">Lorem ipsum dolor sit amet, consectetur adipiscing elit, sed do eiusmod tempor incididunt ut labore et dolore magna aliqua. Ut enim ad minim veniam</p>
  <div class="btn btn-navy" style="left:501px;top:1071px;width:168px;height:46px">LEARN MORE</div>

  <!-- why -->
  <section class="why">
    <div class="why-photo" role="img" aria-label="Student in a yellow sweater writing in a library"></div>
  </section>
  <svg class="abs" style="left:0;top:1196px" width="1200" height="80" viewBox="0 0 1200 80">
    <path d="M0 0 H1200 V30 C900 70 500 10 0 50Z" fill="#f28a23"/>
    <path d="M0 48 C400 18 800 70 1200 28 V46 C800 86 400 36 0 66Z" fill="#7cc20f"/>
    <path d="M0 40 C400 10 800 62 1200 20 V40 C800 78 400 30 0 58Z" fill="#12c3ea"/>
    <path d="M0 32 C400 2 800 54 1200 12 V28 C800 68 400 20 0 48Z" fill="#fff"/>
  </svg>
  <h2 class="why-title display">Why Choose us</h2>
  <p class="why-sub1">Sed ut perspiciatis unde omnis iste</p>
  <p class="why-sub2">natus error sit voluptatem</p>
  <p class="why-text"><b>Lorem Ipsum is simply dummy text of the printing and typesetting industry Lorem Ipsum</b><br>Industry's standard dummy text ever.Lorem Ipsum is simply dummy text of the printing</p>
  <div class="btn btn-green" style="left:145px;top:1636px;width:182px;height:50px">LEARN MORE</div>
  <svg class="abs" style="left:0;top:1820px" width="1200" height="70" viewBox="0 0 1200 70">
    <path d="M0 20 C400 48 800 0 1200 26 V70 H0Z" fill="#fff"/>
    <path d="M0 18 C400 44 800 -2 1200 22 V36 C800 12 400 58 0 32Z" fill="#12c3ea"/>
    <path d="M0 30 C400 56 800 10 1200 34 V46 C800 22 400 66 0 42Z" fill="#7cc20f"/>
    <path d="M0 14 C400 40 800 -6 1200 18 V24 C800 0 400 46 0 20Z" fill="#fff"/>
  </svg>

  <!-- services -->
  <h2 class="section-title display" style="left:0;width:1206px;top:1918px">Our Services</h2>
  <div class="underline" style="left:579px;top:1976px"></div>
  <div class="card c1" style="left:140px;top:2012px" role="img" aria-label="Graduates in caps and gowns"><div class="card-fade"></div><div class="card-label">Our History</div></div>
  <div class="card c2" style="left:457px;top:2012px" role="img" aria-label="Two students walking on campus"><div class="card-fade"></div><div class="card-label">Outcomes</div></div>
  <div class="card c3" style="left:772px;top:2012px" role="img" aria-label="Students working on laptops"><div class="card-fade"></div><div class="card-label">Others</div></div>
  <div class="card c4" style="left:152px;top:2272px" role="img" aria-label="Students talking in a library"><div class="card-fade"></div><div class="card-label">Leadership</div></div>
  <div class="card c5" style="left:468px;top:2272px" role="img" aria-label="Two graduates celebrating"><div class="card-fade"></div><div class="card-label">Scholarships</div></div>
  <div class="card c6" style="left:784px;top:2272px" role="img" aria-label="Student reading at a bright desk"><div class="card-fade"></div><div class="card-label">Support &amp; help</div></div>
  <div class="btn btn-orange" style="left:525px;top:2548px;width:160px;height:44px">VIEW MORE</div>

  <!-- testimonials -->
  <svg class="abs" style="left:0;top:2590px" width="1200" height="540" viewBox="0 0 1200 540">
    <defs><linearGradient id="testimonialBg" x1="0" x2="1" y1="0" y2="0"><stop offset="0" stop-color="#0b4f74"/><stop offset=".5" stop-color="#0a77a8"/><stop offset="1" stop-color="#12c3ea"/></linearGradient></defs>
    <path d="M0 50 C400 70 900 60 1200 0 V480 C800 440 400 520 0 470Z" fill="url(#testimonialBg)"/>
    <path d="M0 470 C400 520 800 440 1200 480 V498 C800 458 400 540 0 488Z" fill="#fff"/>
    <path d="M0 488 C400 540 800 458 1200 498 V512 C800 474 400 555 0 502Z" fill="#0b4f74"/>
    <path d="M0 502 C400 555 800 474 1200 512 V524 C800 488 400 566 0 514Z" fill="#7cc20f"/>
  </svg>
  <div class="quote" style="left:148px;top:2710px">
    <div class="avatar" role="img" aria-label="Portrait photo of Eric"></div>
    <p class="quote-text">“Lorem Ipsum is simply dummy text of the printing and typesetting industry. Lorem Ipsum has been the industry's standard dummy text ever since the 1500s, when an unknown printer stry's standard ustry. Lorem Ipsum has been ndustry's standard dummy”</p>
    <p class="quote-by">By Eric</p>
  </div>
  <div class="quote" style="left:608px;top:2710px">
    <div class="avatar" style="left:30px" role="img" aria-label="Portrait photo of Deb"></div>
    <p class="quote-text" style="left:112px">“Lorem Ipsum is simply dummy text of the printing and typesetting industry. Lorem Ipsum has been the industry's standard dummy text ever since the 1500s, when an unknown printer stry's standard ustry. Lorem Ipsum has been ndustry's standard dummy”</p>
    <p class="quote-by" style="left:112px">By Deb</p>
  </div>

  <!-- latest -->
  <h2 class="section-title display" style="left:0;width:1194px;top:3176px">The Latest</h2>
  <div class="underline" style="left:573px;top:3234px"></div>
  <article class="news n1" style="left:128px;top:3278px" role="img" aria-label="Student writing in a notebook">
    <div class="news-fade"></div><span class="news-date">28 MAY 2021</span>
    <p class="news-text">Lorem ipsum dolor sit amet, con-sectetur adipiscing elit sed do</p>
    <p class="news-more">LEARN MORE →</p>
  </article>
  <article class="news n2" style="left:452px;top:3278px" role="img" aria-label="Students in a bright classroom">
    <div class="news-fade"></div><span class="news-date">28 MAY 2021</span>
    <p class="news-text">Lorem ipsum dolor sit amet, con-sectetur adipiscing elit sed do</p>
    <p class="news-more">LEARN MORE →</p>
  </article>
  <article class="news n3" style="left:776px;top:3278px" role="img" aria-label="Students studying together in a library">
    <div class="news-fade"></div><span class="news-date">28 MAY 2021</span>
    <p class="news-text">Lorem ipsum dolor sit amet, con-sectetur adipiscing elit sed do</p>
    <p class="news-more">LEARN MORE →</p>
  </article>

  <!-- feature -->
  <section class="feature" role="img" aria-label="Student writing with a pencil in a library"></section>
  <svg class="abs" style="left:990px;top:3790px" width="92" height="366" viewBox="0 0 92 366">
    <path d="M0 2 H88 V364 H40" fill="none" stroke="#ee7325" stroke-width="3"/>
  </svg>
  <h2 class="feature-title display">We Empower<br>Eductaion For all</h2>
  <p class="feature-text"><b>Lorem Ipsum is simply dummy text of the printing and typesetting industry Lorem Ipsum</b><br>Industry's standard dummy text ever.Lorem Ipsum is simply dummy text of the printing</p>

  <!-- support -->
  <section class="support"></section>
  <h2 class="support-title display">Education Support<br>is Powerful</h2>
  <p class="support-text"><b>Lorem Ipsum is simply dummy text of the printing and typesetting industry Lorem Ipsum</b><br>Industry's standard dummy text ever.Lorem Ipsum is simply dummy text of the printing</p>
  <div class="btn btn-navy" style="left:124px;top:4605px;width:148px;height:40px">LEARN MORE</div>
  <div class="support-photo" role="img" aria-label="Two graduates celebrating in caps and gowns"></div>

  <!-- footer -->
  <svg class="abs" style="left:0;top:4762px" width="1200" height="80" viewBox="0 0 1200 80">
    <path d="M0 24 C400 0 800 70 1200 30 V80 H0Z" fill="#0b4f74"/>
    <path d="M0 18 C400 -6 800 62 1200 22 V34 C800 74 400 6 0 30Z" fill="#fff"/>
    <path d="M0 30 C400 6 800 74 1200 34 V44 C800 84 400 16 0 40Z" fill="#12c3ea"/>
    <path d="M0 40 C400 16 800 84 1200 44 V52 C800 90 400 24 0 48Z" fill="#7cc20f"/>
  </svg>
  <footer class="footer"></footer>
  <div class="footer-brand"><span class="brand-dot"></span><span class="brand-name">THE HALDEN<br>FOUNDATION</span></div>
  <p class="footer-about">Lorem ipsum dolor sit amet, consectetur adipiscing elit sed do eiusmod tempor incididunt</p>
  <h3 class="col-title display" style="left:452px">Navigation</h3>
  <ul class="col-links" style="left:454px"><li>Services</li><li>About Us</li><li>Donate</li><li>Education</li><li>Blogs</li></ul>
  <h3 class="col-title display" style="left:652px">Resouces</h3>
  <ul class="col-links" style="left:654px"><li>Upcoming Events</li><li>Why We Are</li><li>Resources</li><li>Support</li><li>Contact Us</li></ul>
  <h3 class="col-title display" style="left:868px">Conact Us</h3>
  <p class="col-links" style="left:870px">Email us at<br>enquiry@thehaldenfoundation.org</p>
  <div class="rule"></div>
  <p class="copyright">2021 Copyright © The Halden Foundation | All Right Reserved</p>

</div>
</body>
</html>
```